R Dovak Consulting Design

Our company is a multi-faceted consulting service in specialized areas such as project management and event management.
I would like the design to utilise the colour green, but be simple and unique in concept.
The design should communicate collaboration, openness, trust, efficiency and professionalism.
We like the idea of cogs in a wheel or other geometric designs.

Target Market(s)

Target market is large corporate manufacturers.

Industry/Entity Type

Wheel

Contact Information for Business Card

R Dovak Consulting
Marlene Dovak
Ph. 0438 562 714
Email. marlyfrost@vexorline.on.net
Address. 7 Brambury Ct, Wendale Vic 3299 Australia

```html
<!DOCTYPE html>
<html lang="en">
<head>
<meta charset="utf-8">
<title>R Dovak Consulting – Business Card</title>
<link rel="stylesheet" href="https://fonts.googleapis.com/css2?family=Open+Sans:wght@400;600&family=Exo+2:wght@600&display=swap">
<style>
  :root {
    --bg: #e9e9e9;
    --card: #ffffff;
    --green: #1fa645;
    --text: #3a3a3a;
    --muted: #8a8a8a;
    --deco: #e3e3e3;
  }
  * { box-sizing: border-box; margin: 0; padding: 0; }
  html, body { width: 1200px; height: 1200px; overflow: hidden; }
  body {
    background: radial-gradient(circle at 40% 40%, #f6f6f6 0%, var(--bg) 70%, #d6d6d6 100%);
    font-family: "Open Sans", sans-serif;
    position: relative;
  }
  .card {
    position: absolute;
    left: 250px;
    width: 700px;
    height: 400px;
    background: var(--card);
    box-shadow: 0 10px 30px rgba(0,0,0,0.12);
    overflow: hidden;
  }
  .card--front { top: 150px; }
  .card--back { top: 630px; }

  /* Front */
  .front-rule {
    position: absolute;
    left: 0; right: 0;
    top: 190px;
    height: 4px;
    background: var(--green);
  }
  .wordmark {
    position: absolute;
    display: flex;
    align-items: center;
    gap: 12px;
    background: var(--card);
    font-family: "Exo 2", sans-serif;
    font-weight: 600;
    color: var(--green);
    white-space: nowrap;
  }
  .wordmark__dot {
    width: 18px; height: 18px;
    border-radius: 50%;
    background: var(--green);
    flex: none;
  }
  .card--front .wordmark {
    left: 110px;
    top: 172px;
    padding: 0 16px;
    font-size: 30px;
    line-height: 40px;
  }
  .front-deco {
    position: absolute;
    right: -40px;
    top: 100px;
    width: 300px;
    height: 260px;
    border-radius: 50%;
    background: radial-gradient(circle, var(--deco) 0%, rgba(227,227,227,0) 72%);
  }

  /* Back */
  .back-bar {
    position: absolute;
    left: 120px;
    width: 10px;
    background: var(--green);
  }
  .back-bar--top { top: 0; height: 80px; }
  .back-bar--bottom { bottom: 0; height: 40px; left: 0; width: 50px; height: 8px; bottom: 60px; }
  .contact {
    position: absolute;
    left: 120px;
    top: 110px;
    color: var(--text);
  }
  .contact__name {
    font-size: 22px;
    font-weight: 600;
    margin-bottom: 22px;
  }
  .contact__address {
    font-size: 16px;
    line-height: 22px;
    color: #555;
    margin-bottom: 14px;
  }
  .contact__row {
    display: flex;
    align-items: center;
    gap: 10px;
    font-size: 16px;
    line-height: 28px;
    color: #555;
  }
  .contact__icon {
    width: 22px; height: 22px;
    border-radius: 50%;
    background: var(--green);
    display: flex;
    align-items: center;
    justify-content: center;
    flex: none;
  }
  .card--back .wordmark {
    right: 60px;
    bottom: 70px;
    font-size: 30px;
  }
</style>
</head>
<body>
  <section class="card card--front" aria-label="Business card front">
    <div class="front-deco" role="img" aria-label="Faint grey gear emblem decoration"></div>
    <div class="front-rule"></div>
    <div class="wordmark"><span class="wordmark__dot"></span>R Dovak Consulting</div>
  </section>

  <section class="card card--back" aria-label="Business card back">
    <div class="back-bar back-bar--top"></div>
    <div class="back-bar back-bar--bottom"></div>
    <div class="contact">
      <p class="contact__name">Marlene Dovak</p>
      <p class="contact__address">7 Brambury Ct, Wendale<br>Vic 3299 Australia</p>
      <p class="contact__row">
        <span class="contact__icon">
          <svg width="12" height="12" viewBox="0 0 12 12" aria-hidden="true">
            <rect x="3" y="1" width="6" height="10" rx="1.2" fill="none" stroke="#fff" stroke-width="1.3"/>
            <circle cx="6" cy="9" r="0.8" fill="#fff"/>
          </svg>
        </span>0438 562 714
      </p>
      <p class="contact__row">
        <span class="contact__icon">
          <svg width="12" height="12" viewBox="0 0 12 12" aria-hidden="true">
            <rect x="1" y="3" width="10" height="7" fill="none" stroke="#fff" stroke-width="1.2"/>
            <path d="M1 3 L6 7 L11 3" fill="none" stroke="#fff" stroke-width="1.2"/>
          </svg>
        </span>marlyfrost@vexorline.on.net
      </p>
    </div>
    <div class="wordmark"><span class="wordmark__dot"></span>R Dovak Consulting</div>
  </section>
</body>
</html>
```